Harbormile Trade Associates - Letterhead and Folder

I am looking for letterhead that uses the splash from the logo on the side of the page as well as some information from our website.

I am looking for a folder that is a fold out that has pockets to hold paper as well as a slits for a business card.

Website address is www.harbormiletradeassociates.example

Target Market(s)

Export of Agrifoods, commodities and emergency aid.
Supplying the world food security.

Requirements
Must have
• Use splash and logo, have information about company.
• Letterhead must have splash on a side not in the middle.
Nice to have
• Different pictures that what are provided.

```html
<!DOCTYPE html>
<html lang="en">
<head>
<meta charset="utf-8">
<title>Harbormile Trade Associates – Stationery</title>
<link rel="stylesheet" href="https://fonts.googleapis.com/css2?family=Cinzel:wght@600&family=Open+Sans:wght@400;700&display=swap">
<style>
:root{
  --green:#4ca23f;
  --leaf:#8cc63f;
  --teal:#0c8591;
  --ink:#222;
  --grey:#555;
  --paper:#fff;
  --bg:#e9eaec;
}
*{margin:0;padding:0;box-sizing:border-box}
html,body{width:1200px;height:937px;overflow:hidden;background:var(--bg);font-family:"Open Sans",Arial,sans-serif;color:var(--ink)}
.sheet{position:absolute;background:var(--paper);overflow:hidden}
.brand{font-family:"Cinzel",Georgia,serif;font-weight:600;color:var(--ink);line-height:1.05}
.mark{border-radius:50%;border:3px solid var(--green);flex:none}
.brand-row{position:absolute;display:flex;align-items:center;gap:10px;z-index:1}

/* letterhead */
.letterhead{left:184px;top:66px;width:386px;height:546px}
.letterhead .brand-row{left:18px;top:26px}
.letterhead .mark{width:52px;height:52px}
.letterhead .brand{font-size:13px;width:170px}
.letter{position:absolute;left:37px;top:140px;width:300px;font-size:6px;line-height:1.45;color:var(--grey);z-index:1}
.letter p{margin-bottom:7px}
.letter .gap{margin-bottom:22px}
.letter b{color:var(--ink)}
.signature{width:40px;height:18px;background:linear-gradient(90deg,#ddd,#bbb);margin:4px 0 8px}
.letter-watermark{position:absolute;left:268px;top:150px;width:240px;height:240px;border-radius:50%;border:12px solid rgba(76,162,63,.08)}
.letter-band{position:absolute;left:0;right:0;top:483px;height:44px;display:flex;font-size:7px;color:#fff;line-height:1.3}
.letter-band .contact{background:var(--green);width:194px;display:flex;justify-content:space-around;align-items:center;text-align:center}
.letter-band .address{background:var(--teal);flex:1;display:flex;align-items:center;justify-content:center;text-align:center;font-size:7.5px}

/* folder */
.folder{left:637px;top:41px;width:457px;height:574px}
.folder .mark{position:absolute;left:164px;top:193px;width:120px;height:120px;border-width:5px}
.folder .brand{position:absolute;left:0;right:0;top:330px;text-align:center;font-size:28px}
.folder .brand span{display:block;font-size:16px;letter-spacing:4px;margin-top:6px}
.folder-band{position:absolute;left:0;right:0;top:469px;height:52px;display:flex}
.folder-band .url{background:var(--green);width:265px;display:flex;align-items:center;padding-left:18px;color:#fff;font-size:9.5px;letter-spacing:.8px}
.folder-band .tail{background:var(--teal);flex:1}

/* business cards */
.card{left:45px;width:177px;height:100px;border-radius:8px}
.card-front{top:658px}
.card-front .name{position:absolute;top:12px;width:100%;text-align:center;font-size:8px}
.card-front .role{position:absolute;top:23px;width:100%;text-align:center;font-size:4.5px;font-weight:700}
.card-band{position:absolute;top:32px;left:0;right:0;height:26px;display:flex;font-size:4.5px;color:#fff;line-height:1.3}
.card-band div{display:flex;align-items:center;justify-content:center;text-align:center}
.card-band .g{background:var(--green);width:45%}
.card-band .t{background:var(--teal);flex:1}
.card-front .addr{position:absolute;top:68px;width:100%;text-align:center;font-size:4.5px;line-height:1.5}
.card-back{top:783px}
.card-back .mark{position:absolute;left:35px;top:24px;width:22px;height:22px;border-width:2px}
.card-back .brand{position:absolute;left:10px;top:52px;width:75px;text-align:center;font-size:7px}
.card-back .bar{position:absolute;left:90px;top:38px;width:50px;height:10px;background:var(--green)}
.card-back .bar2{position:absolute;left:140px;top:38px;width:30px;height:10px;background:var(--teal)}

/* envelopes */
.envelope{top:672px;width:432px;height:209px}
.env-front .brand-row{left:14px;top:22px}
.env-front{left:265px}
.env-front .mark{width:42px;height:42px}
.env-front .brand{font-size:12px;width:130px}
.env-watermark{position:absolute;left:265px;top:-20px;width:220px;height:220px;border-radius:50%;border:12px solid rgba(76,162,63,.08)}
.env-back{left:736px}
.env-flap{position:absolute;left:0;right:0;top:0;height:71px;background:var(--teal);border-radius:0 0 0 44px / 0 0 0 40px;display:flex;align-items:center;justify-content:center;color:#fff;font-size:9px;letter-spacing:1.2px}
</style>
</head>
<body>

<section class="sheet letterhead">
  <div class="letter-watermark"></div>
  <div class="brand-row">
    <div class="mark"></div>
    <div class="brand">Harbormile Trade Associates</div>
  </div>
  <div class="letter">
    <p>July 2, 2012</p>
    <p><b>Dear Sir,</b><br>Dock House, Quay Rd., United Kingdom</p>
    <p class="gap">We are pleased to share our latest range of export services for agrifoods, bulk commodities and emergency aid. Our team works with growers, shippers and relief agencies across every continent to move quality goods safely and on time. From sourcing to final delivery, we manage each step with care, so partners can focus on feeding communities and building lasting food security.</p>
    <p class="gap">Please find enclosed our current catalogue and shipping schedule. We would welcome the chance to discuss your needs in more detail.</p>
    <p>Our warehouses in major ports keep stock ready for fast dispatch, and our quality staff inspect every load before it leaves. We hold current certifications for food handling and cold storage, and we report progress to clients at each stage. Thank you for your interest; we look forward to working with you in the season ahead.</p>
    <p>Best Regards,</p>
    <div class="signature" role="img" aria-label="Handwritten signature"></div>
    <p><b>Daniel Reeve</b><br>Director<br>Dock House, Quay Rd., United Kingdom</p>
  </div>
  <div class="letter-band">
    <div class="contact">
      <div>PHONE &amp; FAX<br>+44 20 7946 0811<br>+44 20 7946 0812</div>
      <div>EMAIL &amp; WEB<br>contact@harbormile.example<br>www.harbormile.example</div>
    </div>
    <div class="address"><b>48 Quay Road, Portside 9700<br>UNITED KINGDOM</b></div>
  </div>
</section>

<section class="sheet folder">
  <div class="mark"></div>
  <div class="brand">Harbormile Trade<span>Associates</span></div>
  <div class="folder-band">
    <div class="url">www.harbormiletradeassociates.example</div>
    <div class="tail"></div>
  </div>
</section>

<section class="sheet card card-front">
  <div class="name">SAMIR <b>HOLT</b></div>
  <div class="role">SENIOR GRAPHIC DESIGNER</div>
  <div class="card-band">
    <div class="g">PHONE &amp; FAX<br>+44 20 7946 0811<br>+44 20 7946 0812</div>
    <div class="t">EMAIL &amp; WEB<br>contact@harbormile.example<br>www.harbormile.example</div>
  </div>
  <div class="addr">48 Quay Road, Portside 9700<br><b>UNITED KINGDOM</b></div>
</section>

<section class="sheet card card-back">
  <div class="mark"></div>
  <div class="brand">Harbormile Trade Associates</div>
  <div class="bar"></div><div class="bar2"></div>
</section>

<section class="sheet envelope env-front">
  <div class="env-watermark"></div>
  <div class="brand-row">
    <div class="mark"></div>
    <div class="brand">Harbormile Trade Associates</div>
  </div>
</section>

<section class="sheet envelope env-back">
  <div class="env-flap">www.harbormiletradeassociates.example</div>
</section>

</body>
</html>
```